Bluerock Custom Water Tank

I primarily market the water tanks so want a business care that reflects that. I have attached the water tank logo. You have been working on our water tank so maybe we can use that on the card et. I am leaving as one sided but can be double sided if that works. The information that needs to be on the cards is as follows: Dennis K. Marlow Phone numbers: Office 555-318-4720 Direct 555-260-9134 Mobile 555-482-1657 email address: dennis@fieldgearsupply.example Address P.O. Box 3827 Cedar Hollow, GA 30519 Web Page: www.fieldgearsupply.example. A lot to fit on the card. Thanks

```html
<!DOCTYPE html>
<html lang="en">
<head>
<meta charset="utf-8">
<title>Bluerock Custom Water Tank – Business Card</title>
<link rel="stylesheet" href="https://fonts.googleapis.com/css2?family=Archivo:wght@400;700;800&display=swap">
<style>
  :root {
    --stage: #2a2a2a;
    --card: #111111;
    --card-edge: #1b1b1b;
    --panel: #050505;
    --red: #ff0d0d;
    --white: #f2f2f2;
    --grey: #c9c9c9;
  }
  * { box-sizing: border-box; margin: 0; padding: 0; }
  html, body {
    width: 1200px; height: 1015px; overflow: hidden;
    background: var(--stage);
    font-family: "Archivo", Arial, sans-serif;
  }
  .stage {
    position: relative; width: 1200px; height: 1015px;
    display: flex; flex-direction: column; align-items: center;
    justify-content: center; gap: 56px;
  }
  .card {
    position: relative; width: 760px; height: 434px;
    background: linear-gradient(160deg, var(--card-edge) 0%, var(--card) 55%, #080808 100%);
    box-shadow: 0 18px 40px rgba(0,0,0,.55);
    overflow: hidden;
  }
  /* front */
  .card-front { display: flex; align-items: center; justify-content: center; }
  .brand { display: flex; align-items: center; gap: 18px; }
  .brand-mark { width: 44px; height: 44px; background: var(--red); flex: none; }
  .brand-name {
    color: var(--white); font-weight: 800; font-size: 34px;
    letter-spacing: .5px; text-transform: uppercase; line-height: 1; white-space: nowrap;
  }
  /* back */
  .back-panel { position: absolute; inset: 0; width: 100%; height: 100%; }
  .contact {
    position: absolute; left: 72px; top: 84px; color: var(--white);
  }
  .contact-name {
    color: var(--red); font-weight: 700; font-size: 34px;
    text-transform: uppercase; letter-spacing: .3px; margin-bottom: 18px;
  }
  .contact-address {
    color: var(--grey); font-size: 21px; line-height: 1.25; margin-left: 26px; margin-bottom: 26px;
  }
  .contact-lines { list-style: none; margin-left: 26px; font-size: 21px; line-height: 1.3; }
  .contact-lines li { white-space: nowrap; }
  .contact-lines .label { color: var(--red); font-weight: 700; margin-right: 6px; }
  .contact-lines .accent { color: var(--red); }
</style>
</head>
<body>
<main class="stage">
  <section class="card card-front" aria-label="Card front">
    <div class="brand">
      <span class="brand-mark"></span>
      <span class="brand-name">Bluerock Custom Water Tank</span>
    </div>
  </section>

  <section class="card card-back" aria-label="Card back">
    <svg class="back-panel" viewBox="0 0 760 434" preserveAspectRatio="none" aria-hidden="true">
      <polygon points="500,0 760,0 760,434 505,434 500,160" fill="var(--panel)"/>
      <line x1="500" y1="160" x2="505" y2="434" stroke="#2b2b2b" stroke-width="1"/>
    </svg>
    <div class="contact">
      <h1 class="contact-name">Dennis K. Marlow</h1>
      <p class="contact-address">P.O. Box 3827 Cedar Hollow<br>GA 30519</p>
      <ul class="contact-lines">
        <li><span class="label">P:</span>555-318-4720</li>
        <li><span class="label">P:</span>555-260-9134 <span class="accent">(OFFICE)</span></li>
        <li><span class="label">M:</span>555-482-1657</li>
        <li><span class="label">E:</span>dennis@fieldgearsupply.example</li>
        <li><span class="label">W:</span>www.<span class="accent">fieldgearsupply</span>.example</li>
      </ul>
    </div>
  </section>
</main>
</body>
</html>
```